I am looking for a poster design with a pledge for my clients to take. The pledge will be to not use tanning beds. Our company is a Spray Tanning Salon that focuses on educating our clients on the dangers of indoor tanning while offering a safe alternative through spray tanning. I have an outline of a possible wording but I am VERY open to adjustments on it!
This is not a promotional poster. This is a poster that will be hanging in the salon and our clients will sign around the wall.
Updates

Project Deadline Extended Reason: Not currently in love with any submissions and would like to see more. Looking for a more simple design overall. Added Friday, October 28, 2016

Target Market(s)

Women 20-30 years old

Industry/Entity Type

Salon

Font styles to use
Sans Serif

Requirements
Must have
• Take the pledge to ditch the bed!
• Willowmere Tanning
• **Overall simple design, yet eye catching is requested. Not so busy**
Nice to have
• I am open to different wording!
• I pledge to be timeless
• -UVA rays in tanning beds cause wrinkles and other signs of premature aging
• I pledge to be fearless
• -Using tanning beds can cause severe eye damage, a weakened immune system, and melanoma the deadliest form of skin cancer.
• I pledge to be Sunless!
• -Join the LumaVeil revolution at Willowmere Tanning, Grand Rapids first Sunless Spa Experience.
Should not have
• The photo of the salon on it. I included that photo simply for reference of design, this is where this poster will be hung.

```html
<!DOCTYPE html>
<html lang="en">
<head>
<meta charset="utf-8">
<title>Willowmere Tanning – Take the Pledge</title>
<link href="https://fonts.googleapis.com/css2?family=Antonio:wght@500;700&family=Poppins:ital,wght@1,500&family=Allura&display=swap" rel="stylesheet">
<style>
  :root {
    --cream: #fdfcf6;
    --gold: #a38c5c;
    --gold-deep: #8a6a22;
    --gold-soft: #e9dcbb;
    --ink: #000000;
    --white: #ffffff;
    --brand-green: #2f2f2f;
  }
  html, body {
    margin: 0;
    padding: 0;
    width: 1200px;
    height: 1200px;
    overflow: hidden;
  }
  .poster {
    position: relative;
    width: 1200px;
    height: 1200px;
    background: var(--cream);
    overflow: hidden;
  }
  .poster__backdrop {
    position: absolute;
    inset: 0;
    background:
      radial-gradient(ellipse at 50% 50%, var(--cream) 0%, var(--cream) 45%, var(--gold-soft) 100%);
  }
  .pledge-card {
    position: absolute;
    left: 271px;
    top: 292px;
    width: 687px;
    height: 640px;
    background: var(--white);
  }
  .pledge-card__panel {
    position: absolute;
    left: 10px;
    top: 10px;
    width: 667px;
    height: 620px;
    background: var(--ink);
    color: var(--white);
    text-align: center;
  }
  .pledge {
    position: absolute;
    left: 0;
    width: 100%;
  }
  .pledge__lead {
    margin: 0;
    font-family: "Antonio", "Arial Narrow", sans-serif;
    font-weight: 500;
    font-size: 36px;
    line-height: 40px;
    color: var(--white);
  }
  .pledge__word {
    margin: 0;
    font-family: "Antonio", "Arial Narrow", sans-serif;
    font-weight: 700;
    font-size: 78px;
    line-height: 76px;
    color: var(--gold);
    letter-spacing: -0.5px;
  }
  .pledge__fact {
    margin: 6px 0 0;
    font-family: "Poppins", Arial, sans-serif;
    font-style: italic;
    font-weight: 500;
    font-size: 11.5px;
    line-height: 18px;
    color: var(--white);
  }
  .pledge--timeless { top: 24px; }
  .pledge--fearless { top: 178px; }
  .pledge--sunless  { top: 372px; }
  .pledge-card__rule {
    position: absolute;
    left: 267px;
    top: 526px;
    width: 142px;
    height: 3px;
    background: var(--gold);
  }
  .pledge-card__call {
    position: absolute;
    left: 0;
    top: 536px;
    width: 100%;
    margin: 0;
    font-family: "Allura", cursive;
    font-size: 44px;
    line-height: 60px;
    letter-spacing: 2px;
    color: var(--white);
  }
  .brand {
    position: absolute;
    left: 762px;
    top: 1010px;
    width: 280px;
    height: 80px;
    display: flex;
    align-items: center;
    justify-content: center;
    gap: 12px;
  }
  .brand__mark {
    width: 14px;
    height: 14px;
    background: var(--gold-deep);
  }
  .brand__name {
    font-family: "Antonio", "Arial Narrow", sans-serif;
    font-weight: 500;
    font-size: 34px;
    line-height: 1;
    color: var(--brand-green);
    text-transform: uppercase;
  }
</style>
</head>
<body>
  <main class="poster">
    <div class="poster__backdrop" role="img" aria-label="Background of crossing gold glitter lines on cream"></div>

    <section class="pledge-card">
      <div class="pledge-card__panel">
        <div class="pledge pledge--timeless">
          <p class="pledge__lead">I pledge to be</p>
          <h2 class="pledge__word">TIMELESS</h2>
          <p class="pledge__fact">UVA rays in tanning beds cause wrinkles and other signs of premature aging</p>
        </div>

        <div class="pledge pledge--fearless">
          <p class="pledge__lead">I pledge to be</p>
          <h2 class="pledge__word">FEARLESS</h2>
          <p class="pledge__fact">Using tanning beds can cause severe eye damage, a weakened immune system,<br>and melanoma the deadliest form of skin cancer.</p>
        </div>

        <div class="pledge pledge--sunless">
          <p class="pledge__lead">I pledge to be</p>
          <h2 class="pledge__word">SUNLESS</h2>
          <p class="pledge__fact">Join the LumaVeil revolution at Willowmere Tanning, Grand Rapids first Sunless Spa Experience.</p>
        </div>

        <div class="pledge-card__rule"></div>
        <p class="pledge-card__call">Take the pledge to ditch the bed!</p>
      </div>
    </section>

    <div class="brand">
      <span class="brand__mark"></span>
      <span class="brand__name">Willowmere Tanning</span>
    </div>
  </main>
</body>
</html>
```